Ecommerce Website For Printing Company

Zoravquill.com are a print, design and signage company who sell flyers, business cards, posters, brochures and more to customers in the UK.

Our website is outdated and requires a new design using current web styling and mobile functionality.

We require the following pages to be designed;
- Home Page
- Price Page
- Portfolio Page
- Blog
- Content Page

Our competitors in the printing industry are www.brenticade.com, www.hallowmarsh.co.uk, quorelvane.co.uk, www.tambridok.co.uk

We require the website to give a professional image as well as be easy for customers to navigate, understand and find prices.

Target Market(s)

Businesses

Industry/Entity Type

Printing

Number of Pages Required

4 page

Font styles to use
Sans Serif

Colors
33a6d7

Requirements
Must have
• Popular products, latest news/blog, sales from portfolio, newsletter sign up, footer

```html
<!DOCTYPE html>
<html lang="en">
<head>
<meta charset="utf-8">
<title>Zoravquill.com – Artwork Portfolio</title>
<link href="https://fonts.googleapis.com/css2?family=Open+Sans:wght@400;600;700;800&display=swap" rel="stylesheet">
<style>
:root{
  --brand:#33a6d7;
  --page:#ececec;
  --ink:#444b52;
  --muted:#8a9096;
  --panel-dark:#3a3f44;
  --footer:#2c3034;
  --footer-ink:#9aa1a7;
  --go:#7cc242;
  --white:#ffffff;
  --line:#dcdcdc;
  --bar:#c9cdd1;
}
*{box-sizing:border-box;margin:0;padding:0}
html,body{width:1200px;height:2212px;overflow:hidden}
body{font-family:"Open Sans",Arial,sans-serif;color:var(--ink);background:var(--page);font-size:14px;position:relative}
.utility-bar{height:40px;background:#f6f6f6;border-bottom:1px solid var(--line);display:flex;align-items:center;justify-content:space-between;padding:0 72px;font-size:11px;color:var(--muted)}
.utility-bar .promo{color:var(--brand);font-weight:700;text-transform:uppercase}
.utility-links{display:flex;gap:28px;text-transform:uppercase}
.utility-links .basket{color:var(--ink);font-weight:700}
.site-header{height:110px;background:var(--brand);color:var(--white);position:relative}
.brand{position:absolute;left:72px;top:18px;display:flex;align-items:center;gap:14px}
.brand-name{font-size:40px;font-weight:700;letter-spacing:-1px}
.brand-tag{font-size:10px;font-weight:700;line-height:12px;text-transform:uppercase;border-left:2px solid rgba(255,255,255,.6);padding-left:10px}
.call{position:absolute;right:72px;top:18px;font-size:24px}
.main-nav{position:absolute;right:72px;bottom:18px;display:flex;gap:30px;font-size:14px;font-weight:600;align-items:center}
.main-nav .active{background:var(--white);color:var(--brand);padding:4px 10px}
.layout{position:absolute;top:180px;left:72px;width:1056px}
.sidebar{position:absolute;left:0;top:0;width:248px}
.rates{background:var(--panel-dark);color:var(--white);padding-bottom:24px}
.rates h2{font-size:20px;font-weight:700;padding:14px 20px;background:#2e3236;text-transform:uppercase}
.rates .group{display:block;color:var(--brand);font-weight:700;padding:12px 20px 4px;font-size:15px}
.rates .group.open{background:var(--brand);color:var(--white);padding:8px 20px;margin-top:10px}
.rates ul{list-style:none;padding:6px 20px 6px 28px}
.rates li{font-size:13px;line-height:26px;color:#d6d9dc;position:relative}
.rates li::before{content:"›";position:absolute;left:-12px;color:var(--brand)}
.ad{background:var(--white);padding:12px;margin:56px auto 0;width:200px;box-shadow:0 1px 3px rgba(0,0,0,.1)}
.ad .art{height:252px;position:relative;overflow:hidden;text-align:center}
.getaway .art{background:linear-gradient(180deg,#eef7fb 0%,#eef7fb 52%,#2aa2d4 52%,#2aa2d4 100%)}
.getaway .headline{position:absolute;left:0;right:0;top:34px;font-size:24px;font-weight:800;line-height:26px;color:#1f3d5a}
.getaway .from{position:absolute;left:0;right:0;top:96px;font-size:14px;font-weight:700;color:#e25b2a}
.getaway .beach{position:absolute;left:0;right:0;bottom:0;height:60px;background:#f1d48a}
.getaway .cta{position:absolute;left:30px;right:30px;top:150px;height:26px;background:#f6c93a;font-size:11px;font-weight:700;line-height:26px;color:#1f3d5a}
.venue .art{background:#f4f1e2}
.venue .site{position:absolute;left:0;right:0;top:20px;font-size:16px;font-weight:700;color:#4a5a20}
.venue .fields{position:absolute;left:14px;right:14px;top:56px;height:110px;background:linear-gradient(180deg,#c8dc7a,#7a9a2e)}
.venue .name{position:absolute;left:0;right:0;top:184px;font-size:20px;font-weight:700;color:#4a5a20}
.venue .sub{position:absolute;left:40px;right:40px;top:220px;height:4px;background:#b9c48c}
.content{position:absolute;left:268px;top:0;width:788px}
.hero{height:160px;background:linear-gradient(120deg,#d9dfe3 0%,#f2f4f5 50%,#bfc9cf 100%);position:relative;overflow:hidden}
.hero .desk{position:absolute;inset:0}
.hero-title{position:absolute;left:16px;top:16px;background:rgba(255,255,255,.92);color:var(--brand);font-size:22px;font-weight:800;line-height:26px;padding:12px 20px;text-transform:uppercase}
.filters{display:flex;justify-content:space-between;margin-top:40px}
.search,.select{height:32px;background:var(--white);border:1px solid var(--line);display:flex;align-items:center;justify-content:space-between;padding:0 10px;font-size:11px;color:var(--muted)}
.search{width:300px}.select{width:120px}
.category{margin-top:28px}
.category-head{height:32px;background:var(--white);display:flex;align-items:center;justify-content:space-between;padding:0 10px 0 14px;border-left:4px solid var(--brand)}
.category-head h3{font-size:15px;font-weight:700;color:var(--brand);text-transform:uppercase}
.pager{display:flex;gap:3px}
.pager span{width:18px;height:18px;background:#9aa0a5;color:var(--white);font-size:12px;line-height:18px;text-align:center}
.cards{display:grid;grid-template-columns:repeat(3,1fr);gap:19px;margin-top:12px}
.card{background:var(--white);height:290px;padding:14px;box-shadow:0 1px 3px rgba(0,0,0,.08)}
.card .art{height:218px;position:relative;overflow:hidden}
.card p{font-size:13px;text-align:center;margin-top:14px}
.sheet{position:absolute;background:var(--white);box-shadow:0 2px 7px rgba(0,0,0,.28);overflow:hidden;padding:8px}
.bar{display:block;height:4px;background:var(--bar);margin:5px 0;border-radius:1px}
.bar.s{width:55%}.bar.m{width:75%}
.photo{display:block;width:100%}
.title{display:block;font-weight:800;line-height:1.1}
.mark{display:block;width:12px;height:12px;background:var(--brand);margin-bottom:6px}
.logo-card{position:absolute;left:14px;right:14px;top:44px;height:130px;display:flex;align-items:center;justify-content:center;font-size:20px;font-weight:600;box-shadow:0 2px 7px rgba(0,0,0,.25)}
.newsletter{position:absolute;top:1928px;left:0;width:1200px;height:60px;background:var(--brand);display:flex;align-items:center;padding:0 72px;gap:24px;color:var(--white)}
.newsletter h2{font-size:18px;font-weight:700;text-transform:uppercase;width:200px}
.email{width:240px;height:30px;background:var(--white);color:var(--muted);font-size:11px;display:flex;align-items:center;padding:0 10px}
.opt{display:flex;align-items:center;gap:8px;font-size:12px;margin-left:18px}
.opt i{width:14px;height:14px;background:var(--white);display:block}
.signup{margin-left:auto;width:150px;height:30px;background:var(--go);font-weight:700;font-size:13px;display:flex;align-items:center;justify-content:center;text-transform:uppercase}
.site-footer{position:absolute;top:1988px;left:0;width:1200px;height:224px;background:var(--footer);color:var(--footer-ink);text-align:center;font-size:12px;padding-top:28px}
.footer-links{display:flex;justify-content:center;gap:22px}
.footer-links+.footer-links{margin-top:10px}
.social{display:flex;justify-content:center;gap:14px;margin-top:26px}
.social span{width:30px;height:30px;border-radius:50%;background:#51575c;display:block}
.legal{margin-top:22px;font-size:10px;line-height:16px;color:#6f767c}
</style>
</head>
<body>
<div class="utility-bar">
  <span class="promo">Free shipping on all orders over £50</span>
  <nav class="utility-links"><span>Live chat</span><span>Support</span><span>Track orders</span><span>Your account</span><span class="basket">Basket £0.00</span></nav>
</div>

<header class="site-header">
  <div class="brand"><span class="brand-name">Zoravquill.com</span><span class="brand-tag">Print<br>Design<br>Signage<br>Websites</span></div>
  <div class="call">Call us : 01632 960 450</div>
  <nav class="main-nav">
    <span>Home</span><span>About</span><span>Printing</span><span class="active">Graphic design</span><span>Website design</span><span>Artwork guide</span>
    <svg width="16" height="16" viewBox="0 0 16 16" aria-hidden="true"><circle cx="6.5" cy="6.5" r="5" fill="none" stroke="#fff" stroke-width="2"/><line x1="10.5" y1="10.5" x2="15" y2="15" stroke="#fff" stroke-width="2"/></svg>
  </nav>
</header>

<div class="layout">
  <aside class="sidebar">
    <div class="rates">
      <h2>All rates</h2>
      <span class="group">Large Format</span>
      <span class="group open">Popular Products</span>
      <ul>
        <li>Flyer Printing</li><li>Folded Flyers</li><li>Brochure Printing</li><li>Poster Printing</li>
        <li>Business Cards</li><li>Letterhead Printing</li><li>Compliment Slips</li><li>Rollup Banners</li>
        <li>Invoice Pads &amp; NCR Pads</li><li>Stickers and Labels</li><li>Presentation Folders</li><li>Christmas Cards</li>
      </ul>
      <span class="group">Canvas Prints</span>
    </div>
    <div class="ad getaway"><div class="art">
      <span class="headline">WEEKEND<br>GETAWAYS</span>
      <span class="from">FROM £128</span>
      <span class="cta">BOOK YOUR STAY</span>
      <span class="beach" role="img" aria-label="Beach scene"></span>
    </div></div>
    <div class="ad venue"><div class="art">
      <span class="site">Zoravquill.com</span>
      <span class="fields" role="img" aria-label="Countryside fields photo"></span>
      <span class="name">Willowmere Barn</span>
      <span class="sub"></span>
    </div></div>
  </aside>

  <main class="content">
    <section class="hero">
      <div class="desk" role="img" aria-label="Designer desk with pens and printed artwork"></div>
      <h1 class="hero-title">Artwork<br>Portfolio</h1>
    </section>

    <div class="filters">
      <div class="search">Find portfolio (e.g. logo)
        <svg width="12" height="12" viewBox="0 0 16 16" aria-hidden="true"><circle cx="6.5" cy="6.5" r="5" fill="none" stroke="#8a9096" stroke-width="2"/><line x1="10.5" y1="10.5" x2="15" y2="15" stroke="#8a9096" stroke-width="2"/></svg>
      </div>
      <div class="select">Ordering <span>▾</span></div>
    </div>

    <section class="category">
      <div class="category-head"><h3>Accountancy and Financial</h3><div class="pager"><span>‹</span><span>›</span></div></div>
      <div class="cards">
        <div class="card"><div class="art">
          <div class="sheet" style="left:18px;top:50px;width:140px;height:82px"><span class="mark"></span><span class="title" style="font-size:10px;color:#1f3d5a">Quarrymede</span><span class="bar m"></span><span class="bar s"></span></div>
          <div class="sheet" style="left:60px;top:104px;width:140px;height:82px;background:#1f3d5a"><span class="bar m" style="background:#6f8aa3"></span><span class="bar s" style="background:#6f8aa3"></span><span class="bar m" style="background:#6f8aa3"></span></div>
        </div><p>Quarrymede (Business Cards)</p></div>
        <div class="card"><div class="art">
          <div class="sheet" style="left:50px;top:10px;width:122px;height:198px;background:#5b2c6f;padding:10px">
            <span class="title" style="font-size:13px;color:#f3c64a">GET YOUR<br>TAX RIGHT</span>
            <span class="photo" style="height:78px;margin:8px 0;background:#b0306f" role="img" aria-label="Office photo"></span>
            <span class="bar m" style="background:#a98bb8"></span><span class="bar s" style="background:#a98bb8"></span><span class="bar m" style="background:#a98bb8"></span>
          </div>
        </div><p>Holloway and Brisk</p></div>
        <div class="card"><div class="art">
          <div class="sheet" style="left:28px;top:16px;width:120px;height:170px"><span class="mark"></span><span class="bar s"></span><span class="bar m" style="margin-top:20px"></span><span class="bar m"></span><span class="bar"></span></div>
          <div class="sheet" style="left:72px;top:36px;width:120px;height:170px"><span class="mark"></span><span class="title" style="font-size:9px;color:#1f3d5a">Quarrymede</span><span class="bar m" style="margin-top:18px"></span><span class="bar"></span><span class="bar s"></span><span class="bar m"></span></div>
        </div><p>Quarrymede (Letterheads)</p></div>
      </div>
    </section>

    <section class="category">
      <div class="category-head"><h3>Charity</h3><div class="pager"><span>‹</span><span>›</span></div></div>
      <div class="cards">
        <div class="card"><div class="art">
          <div class="sheet" style="left:10px;top:58px;width:100px;height:110px;background:#d4462f"><span class="title" style="font-size:18px;color:#fff">KIP</span><span class="bar m" style="background:#f0a08f"></span><span class="bar s" style="background:#f0a08f"></span></div>
          <div class="sheet" style="left:110px;top:58px;width:100px;height:110px"><span class="photo" style="height:48px;background:#f3c64a" role="img" aria-label="Event photo"></span><span class="bar m"></span><span class="bar"></span><span class="bar s"></span></div>
        </div><p>KIP</p></div>
        <div class="card"><div class="art">
          <div class="sheet" style="left:50px;top:10px;width:122px;height:198px;background:#7b3fa0;padding:10px">
            <span class="title" style="font-size:13px;color:#f7e04a">SPEAK UP<br>WE LISTEN</span>
            <span class="photo" style="height:82px;margin:8px 0;background:#d98ac0" role="img" aria-label="Group photo"></span>
            <span class="bar m" style="background:#c6a2dc"></span><span class="bar s" style="background:#c6a2dc"></span>
          </div>
        </div><p>Ashvale Advocacy</p></div>
        <div class="card"><div class="art">
          <div class="sheet" style="left:50px;top:10px;width:122px;height:198px;background:#8fc23c;padding:10px">
            <span class="title" style="font-size:13px;color:#1e4a1a">YOUTH<br>CLUB</span>
            <span class="photo" style="height:70px;margin:8px 0;background:#f0d23a" role="img" aria-label="Activity photo"></span>
            <span class="bar m" style="background:#d8ec9f"></span><span class="bar" style="background:#d8ec9f"></span><span class="bar s" style="background:#d8ec9f"></span>
          </div>
        </div><p>Thornbury Youth Project</p></div>
      </div>
    </section>

    <section class="category">
      <div class="category-head"><h3>Education</h3><div class="pager"><span>‹</span><span>›</span></div></div>
      <div class="cards">
        <div class="card"><div class="art">
          <div class="sheet" style="left:14px;top:46px;width:194px;height:124px;background:#f7e04a">
            <span class="title" style="font-size:12px;color:#2a5d8f">Welcome to our school</span>
            <span class="photo" style="height:50px;margin:6px 0;background:#e8a52a" role="img" aria-label="Classroom photo"></span>
            <span class="bar m" style="background:#c9a83a"></span><span class="bar s" style="background:#c9a83a"></span>
          </div>
        </div><p>Marlow Brook Primary School</p></div>
        <div class="card"><div class="art">
          <div class="sheet" style="left:10px;top:60px;width:68px;height:100px"><span class="bar" style="background:var(--brand)"></span><span class="bar m"></span><span class="bar"></span><span class="bar s"></span></div>
          <div class="sheet" style="left:78px;top:60px;width:68px;height:100px"><span class="bar m"></span><span class="bar"></span><span class="bar s"></span></div>
          <div class="sheet" style="left:146px;top:60px;width:68px;height:100px;background:#2a5d8f"><span class="bar m" style="background:#7fa6c9"></span><span class="bar s" style="background:#7fa6c9"></span></div>
          <svg style="position:absolute;left:98px;top:98px" width="26" height="26" viewBox="0 0 26 26" aria-hidden="true"><circle cx="13" cy="13" r="12" fill="#2a5d8f"/><path d="M10 7l7 6-7 6" fill="none" stroke="#fff" stroke-width="2.5"/></svg>
        </div><p>Ferngate Lane</p></div>
        <div class="card"><div class="art">
          <div class="sheet" style="left:50px;top:10px;width:122px;height:198px;background:#3f8d3a;padding:10px">
            <span class="title" style="font-size:12px;color:#fff">Little Acorns<br>Start Here</span>
            <span class="photo" style="height:86px;margin:8px 0;background:#9ccc5f" role="img" aria-label="Nursery garden photo"></span>
            <span class="bar m" style="background:#a7d08a"></span><span class="bar s" style="background:#a7d08a"></span>
          </div>
        </div><p>Birchfield Nursery</p></div>
      </div>
    </section>

    <section class="category">
      <div class="category-head"><h3>Logo</h3><div class="pager"><span>‹</span><span>›</span></div></div>
      <div class="cards">
        <div class="card"><div class="art"><div class="logo-card" style="background:#6a1e6e;color:#f3d3ea">Plum Petals</div></div><p>Business Stationery</p></div>
        <div class="card"><div class="art"><div class="logo-card" style="background:#1b1b1b;color:#ffffff">Vantor</div></div><p>Flyer Printing and Leaflet</p></div>
        <div class="card"><div class="art"><div class="logo-card" style="background:#fbf5ec;color:#b0306f">Cedarline</div></div><p>Flyer Printing and Leaflet</p></div>
      </div>
    </section>
  </main>
</div>

<section class="newsletter">
  <h2>Our Newsletter</h2>
  <div class="email">Enter your Email ID</div>
  <span class="opt"><i></i>Offers</span>
  <span class="opt"><i></i>Printing news</span>
  <span class="opt"><i></i>All</span>
  <div class="signup">Sign up</div>
</section>

<footer class="site-footer">
  <nav class="footer-links"><span>About</span><span>Printing</span><span>Graphic Design</span><span>Website design</span><span>Artwork guide</span><span>Terms of use</span><span>Samples</span><span>Testimonials</span><span>Blog</span><span>Contact Us</span></nav>
  <nav class="footer-links"><span>Special Offers</span><span>Terms and Conditions</span><span>Privacy Policy</span><span>Trade account</span></nav>
  <div class="social"><span></span><span></span><span></span><span></span><span></span><span></span></div>
  <p class="legal">Zoravquill.com is a trading name of Zoravquill Print Ltd. Registered in England and Wales.<br>All prices exclude VAT unless stated. Copyright 2024 Zoravquill.com. All rights reserved.</p>
</footer>
</body>
</html>
```